Bring my website out of the dark ages!

Website redesign for Velmar Consulting
www.velmarqx.com and www.trundlebox.ca
Currently dark (black), small font, boring, old
Want something simple, bright, fun, modern, clean and professional
Flexible content, any ideas appreciated
In business since 1998, focused on long term client relationships and being there when it matters.
Specialize solutions for clients based on their needs, vision and budget, not what the IT market thinks is the latest and greatest (and most profitable).
Want to eventually add helpful content (videos) and testimonials to the site for the benefit of the visitor

Target Market(s)

Anyone looking for IT services - target is a business with 25-100 employees.

Industry/Entity Type

It Company

Coding

Coded - Design and coding required

Number of Pages Required

4 page

Colors

Designer to choose colors to be used in the design.

Requirements
Must have
• Bright, clean, simple, no scrolling, fast
Nice to have
• Neat animation of some kind
Should not have
• scrolling
• too much information

```html
<!DOCTYPE html>
<html lang="en">
<head>
<meta charset="utf-8">
<title>Velmar Consulting</title>
<link rel="stylesheet" href="https://fonts.googleapis.com/css2?family=Open+Sans:wght@400;600;700;800&display=swap">
<style>
:root{
  --ink:#2b2b2b;
  --text:#444;
  --muted:#8a8a8a;
  --accent:#f0a43a;
  --band:#ececec;
  --card:#ffffff;
  --dark:#262626;
  --white:#ffffff;
  --line:#3a3a3a;
}
*{box-sizing:border-box;margin:0;padding:0}
html,body{width:1200px;height:2985px;overflow:hidden;background:var(--white)}
body{position:relative;font-family:"Open Sans",Arial,sans-serif;color:var(--text)}
.abs{position:absolute}

/* header */
.site-header{position:absolute;left:0;top:0;width:1200px;height:80px;background:var(--white)}
.brand{position:absolute;left:134px;top:18px;display:flex;align-items:center;gap:10px}
.brand-dot{width:14px;height:14px;border-radius:50%;background:var(--accent)}
.brand-name{font-size:24px;font-weight:400;color:#6d6d6d;letter-spacing:.5px}
.top-contact{position:absolute;right:134px;top:16px;display:flex;gap:22px;font-size:14px;font-weight:600;color:#444}
.top-contact span{display:flex;align-items:center;gap:6px}
.main-nav{position:absolute;right:134px;top:50px;display:flex;gap:26px;font-size:11.5px;text-transform:uppercase;color:#555}
.main-nav .current{color:var(--accent)}

/* hero */
.hero{position:absolute;left:0;top:80px;width:1200px;height:615px;
  background:linear-gradient(100deg,#2d3440 0%,#56606c 35%,#a9b2bd 62%,#7e8894 80%,#4a525c 100%);
  clip-path:polygon(0 0,100% 0,100% 540px,0 615px)}
.hero-title{position:absolute;left:134px;top:208px;color:var(--white);font-size:27px;font-weight:800;line-height:34px;text-transform:uppercase;letter-spacing:.3px}
.btn{display:inline-block;border:1px solid #bbb;font-size:12.5px;font-weight:600;text-transform:uppercase;text-align:center}
.hero-cta{position:absolute;left:134px;top:288px;width:108px;height:38px;line-height:36px;background:var(--white);color:#333;border:none}
.slide-arrow{position:absolute;top:252px;width:26px;height:26px;background:rgba(0,0,0,.55)}

/* headings */
.section-title{position:absolute;left:0;width:1200px;text-align:center;font-size:27px;font-weight:800;color:var(--ink);text-transform:uppercase}

/* welcome */
.welcome-text{position:absolute;left:134px;top:800px;width:932px;font-size:14.5px;line-height:25px;text-align:justify;text-align-last:center;color:#444}
.video{position:absolute;left:336px;top:923px;width:530px;height:306px;background:linear-gradient(135deg,#5a4a6a 0%,#2c3a52 45%,#1c2a36 75%,#2c3a30 100%)}
.play{position:absolute;left:580px;top:1057px;width:42px;height:42px}

/* services */
.services-band{position:absolute;left:0;top:1310px;width:1200px;height:774px;background:var(--band);
  clip-path:polygon(0 77px,100% 0,100% 690px,0 774px)}
.service-card{position:absolute;width:299px;height:193px;background:var(--card);box-shadow:0 1px 3px rgba(0,0,0,.08);text-align:center}
.service-card svg{position:absolute;left:114px;top:26px;width:72px;height:72px}
.service-card h3{position:absolute;left:20px;right:20px;top:118px;font-size:15.5px;font-weight:600;line-height:22px;color:#333}

/* testimonials */
.testimonial{position:absolute;top:2200px;width:299px;height:180px;background:var(--band);
  clip-path:polygon(0 12%,24% 0,76% 0,100% 12%,100% 88%,76% 100%,24% 100%,0 88%);text-align:center}
.testimonial p{position:absolute;left:34px;right:34px;top:54px;font-size:11px;font-weight:700;line-height:17px;color:#333}
.testimonial cite{position:absolute;left:0;right:0;top:112px;font-style:normal;font-size:11.5px;color:var(--muted)}
.view-all{position:absolute;left:546px;top:2411px;width:110px;height:37px;line-height:35px;color:#777;background:var(--white)}

/* contact */
.contact-band{position:absolute;left:0;top:2505px;width:1200px;height:480px;background:var(--band);
  clip-path:polygon(0 78px,100% 0,100% 100%,0 100%)}
.contact-col{position:absolute;top:2668px;font-size:12.5px;line-height:19px;color:#555}
.contact-col a{display:block;margin-top:4px;font-size:16px;font-weight:600;color:#111;text-decoration:none}

/* footer */
.site-footer{position:absolute;left:0;top:2816px;width:1200px;height:169px;background:var(--dark);
  clip-path:polygon(0 56px,100% 0,100% 100%,0 100%)}
.footer-nav{position:absolute;left:134px;top:2906px;font-size:10.5px;color:#aaa;display:flex;gap:9px}
.copyright{position:absolute;left:134px;top:2934px;font-size:10.5px;color:#999}
.social{position:absolute;left:946px;top:2920px;display:flex;gap:16px}
.social span{width:16px;height:16px;border-radius:50%;background:#9a9a9a}
</style>
</head>
<body>

<header class="site-header">
  <div class="brand"><span class="brand-dot"></span><span class="brand-name">Velmar Consulting</span></div>
  <div class="top-contact">
    <span><svg width="13" height="13" viewBox="0 0 24 24"><path fill="#555" d="M6.6 10.8a15 15 0 0 0 6.6 6.6l2.2-2.2c.3-.3.7-.4 1-.2 1.1.4 2.3.6 3.6.6.6 0 1 .4 1 1V20c0 .6-.4 1-1 1A17 17 0 0 1 3 4c0-.6.4-1 1-1h3.5c.6 0 1 .4 1 1 0 1.3.2 2.5.6 3.6.1.3 0 .7-.2 1z"/></svg>587-410-2293</span>
    <span><svg width="14" height="12" viewBox="0 0 24 20"><path fill="#555" d="M2 0h20a2 2 0 0 1 2 2v1L12 10 0 3V2a2 2 0 0 1 2-2zm-2 5.5 12 7 12-7V18a2 2 0 0 1-2 2H2a2 2 0 0 1-2-2z"/></svg>helpdesk@velmarqx.com</span>
  </div>
  <nav class="main-nav"><span class="current">Home</span><span>About</span><span>Services</span><span>Resources</span><span>Contact</span></nav>
</header>

<section class="hero" role="img" aria-label="Technician holding a network server unit in a data centre aisle">
  <h1 class="hero-title">Suspendisse gravida<br>ornare erat sed pulvinar</h1>
  <span class="btn hero-cta">Contact us</span>
</section>
<svg class="slide-arrow" style="left:0" viewBox="0 0 26 26"><path d="M17 13H9m3-4-4 4 4 4" stroke="#fff" stroke-width="2" fill="none"/></svg>
<svg class="slide-arrow" style="right:0" viewBox="0 0 26 26"><path d="M9 13h8m-3-4 4 4-4 4" stroke="#fff" stroke-width="2" fill="none"/></svg>

<h2 class="section-title" style="top:758px">Welcome to Velmar</h2>
<p class="welcome-text">Velmar knows that a business builds its foundation with information and communication. You need the right technology to succeed in today's world. We establish long term partnerships with our clients to deliver operational efficiencies, reduce complexities and increase productivity.&nbsp; Velmar's services are focused on the needs of small and medium sized businesses. We specialize in the entire range of IT consulting including managed services and technical projects.</p>
<div class="video" role="img" aria-label="Video still of a person working at desktop monitors in a dim office"></div>
<svg class="play" viewBox="0 0 42 42"><circle cx="21" cy="21" r="20" fill="#fff"/><path d="M16 12l13 9-13 9z" fill="#222"/></svg>

<div class="services-band"></div>
<h2 class="section-title" style="top:1458px">Services</h2>

<article class="service-card" style="left:134px;top:1518px">
  <svg viewBox="0 0 72 72" fill="none" stroke="#333" stroke-width="2"><rect x="6" y="8" width="52" height="36" rx="2"/><path d="M6 38h52M26 44v8h12v-8M20 52h24"/><path d="M22 20l-5 5 5 5M34 20l5 5-5 5M30 18l-4 14"/><circle cx="56" cy="54" r="7"/><circle cx="56" cy="54" r="2.5"/><path d="M56 44v3M56 61v3M46 54h3M63 54h3"/></svg>
  <h3>Computer Installation &amp; Deployment</h3>
</article>
<article class="service-card" style="left:451px;top:1518px">
  <svg viewBox="0 0 72 72" fill="none" stroke="#333" stroke-width="2"><path d="M14 10a10 10 0 0 0 12 14l30 30a4 4 0 0 0 6-6L32 18A10 10 0 0 0 18 6l6 6-2 6-6 2z"/><path d="M56 8l8 8-6 4-18 18-4-4 18-18z"/><path d="M34 40L14 60a3 3 0 0 1-4-4l20-20"/></svg>
  <h3>Computer Maintenance &amp; Support</h3>
</article>
<article class="service-card" style="left:768px;top:1518px">
  <svg viewBox="0 0 72 72" fill="none" stroke="#333" stroke-width="2"><rect x="10" y="6" width="52" height="12" rx="2"/><rect x="10" y="22" width="52" height="12" rx="2"/><rect x="10" y="38" width="52" height="12" rx="2"/><path d="M16 12h24M16 28h24M16 44h24M36 50v8M8 62h56"/><circle cx="52" cy="12" r="2"/><circle cx="52" cy="28" r="2"/><circle cx="52" cy="44" r="2"/><circle cx="36" cy="62" r="3"/></svg>
  <h3>Server Configuration &amp; Administration</h3>
</article>
<article class="service-card" style="left:134px;top:1733px">
  <svg viewBox="0 0 72 72" fill="none" stroke="#333" stroke-width="2"><path d="M10 10h40v32H26l-10 8v-8h-6z"/><path d="M54 22h8v30h-6v8l-10-8H28v-6"/><circle cx="30" cy="26" r="6"/><circle cx="30" cy="26" r="2"/><path d="M30 16v3M30 33v3M20 26h3M37 26h3"/></svg>
  <h3 style="top:128px">Desktop Support</h3>
</article>
<article class="service-card" style="left:451px;top:1733px">
  <svg viewBox="0 0 72 72" fill="none" stroke="#333" stroke-width="2"><path d="M20 42a12 12 0 0 1 0-24 16 16 0 0 1 30-2 12 12 0 0 1 2 26z"/><path d="M24 42v10M36 42v14M48 42v10M30 42v6M42 42v6"/><circle cx="24" cy="55" r="3"/><circle cx="36" cy="59" r="3"/><circle cx="48" cy="55" r="3"/></svg>
  <h3 style="top:128px">Network Support</h3>
</article>
<article class="service-card" style="left:768px;top:1733px">
  <svg viewBox="0 0 72 72" fill="none" stroke="#333" stroke-width="2"><path d="M36 6l24 8v18c0 16-10 26-24 32C22 58 12 48 12 32V14z"/><path d="M36 12l18 6v14c0 12-8 20-18 25-10-5-18-13-18-25V18z"/><rect x="27" y="32" width="18" height="14" rx="1"/><path d="M30 32v-5a6 6 0 0 1 12 0v5"/></svg>
  <h3>Security &amp; Backup Solutions</h3>
</article>

<h2 class="section-title" style="top:2148px">Testimonials</h2>
<blockquote class="testimonial" style="left:134px"><p>" Fusce nec leo ac urna pulvinar auctor. Mauris bibendum fringilla velit. Nulla in lorem at massa pellentesque posuere. "</p><cite>Aaron Pell, Company name</cite></blockquote>
<blockquote class="testimonial" style="left:451px"><p>" Fusce nec leo ac urna pulvinar auctor. Mauris bibendum fringilla velit. Nulla in lorem at massa pellentesque posuere. "</p><cite>Aaron Pell, Company name</cite></blockquote>
<blockquote class="testimonial" style="left:768px"><p>" Fusce nec leo ac urna pulvinar auctor. Mauris bibendum fringilla velit. Nulla in lorem at massa pellentesque posuere. "</p><cite>Aaron Pell, Company name</cite></blockquote>
<span class="btn view-all">View all</span>

<div class="contact-band"></div>
<h2 class="section-title" style="top:2614px">Contact</h2>
<div class="contact-col" style="left:134px">For Inquiries Related to Monthly<br>Maintenance Services<a>info@velmarqx.com</a></div>
<div class="contact-col" style="left:374px">For Inquiries Related to<br>Procurement<a>purchasing@velmarqx.com</a></div>
<div class="contact-col" style="left:636px">For any other networking or<br>computer needs<a>helpdesk@velmarqx.com</a></div>
<div class="contact-col" style="left:874px">For any suggestions or feedback<br>email us at<a>l@velmarqx.com</a></div>

<footer class="site-footer"></footer>
<nav class="footer-nav"><span>Home</span><span>|</span><span>About</span><span>|</span><span>Services</span><span>|</span><span>Resources</span><span>|</span><span>Contact</span></nav>
<p class="copyright">Copyright © 2018 Velmar Consulting. All rights reserved.</p>
<div class="social"><span></span><span></span><span></span><span></span></div>

</body>
</html>
```